Pediatric Vision Care: Myopia Control Brochure

We are a pediatric eye care practice (ophthalmology and optometry). One of our services we offer for children is myopia control, which are strategies for slowing or stopping the progression of nearsightedness. This is a service we need to sell to parents because most insurance won't pay for it. There are different options we offer that can work well for kids in different situations: glasses with Corvane lenses, atropine eye drops, and/or special contact lenses. We need a brochure we can distribute to parents to let them know about this service that would encourage them to buy it for children who need it. Attached is our initial draft brochure created by our staff that provides text that we want to keep. The images and layout can change. We probably need at least one or two photos of kids on the brochure, because this is only something that works for children who are still growing, and the target audience is parents of 4-8 year old children.

Target Market(s)

Parents of 4-8 year old children

Font styles to use
Sans Serif

Requirements
Must have
• I'm uploading our company logo that should be included somewhere on the brochure. You can include contact information (web address, phone number) for our practice that is found on our website: http://www.brookhollowkidsvision.com/
Should not have
• This should not look childish. We need the impression to be friendly but professional, medical, expert.

```html
<!DOCTYPE html>
<html lang="en">
<head>
<meta charset="utf-8">
<title>Myopia Control Brochure</title>
<link href="https://fonts.googleapis.com/css2?family=Poppins:wght@300;400;500;600;700&display=swap" rel="stylesheet">
<style>
:root{
  --navy:#1b3057;
  --green:#a8cf8a;
  --green-line:#8cc63f;
  --orange:#f07b22;
  --gold:#f3b41b;
  --peach:#f8dcc0;
  --lavender:#dedbee;
  --ink:#4a4f5a;
  --bg:#eeeff1;
}
*{box-sizing:border-box;margin:0;padding:0}
html,body{width:887px;height:1200px;overflow:hidden;background:var(--bg);font-family:"Poppins",sans-serif;color:var(--ink)}
.sheet{position:absolute;left:101px;width:692px;height:537px;background:#fff;box-shadow:0 3px 10px rgba(0,0,0,.12);overflow:hidden}
.sheet--outer{top:48px}
.sheet--inner{top:614px}
.abs{position:absolute}
.brand{display:flex;align-items:center;gap:6px;color:var(--navy);font-weight:500;font-size:12px;line-height:1.1}
.brand__dot{width:12px;height:12px;border-radius:50%;background:var(--green-line);flex:none}
.body{font-size:8.3px;line-height:1.3;font-weight:300;color:var(--ink);z-index:2}
.body--just{text-align:justify}
.body b{font-weight:600;color:#333}
.panel-title{font-weight:500;color:var(--navy)}
.rule{height:2px;width:20px;background:var(--orange)}
.photo{position:absolute}
.footer{position:absolute;left:0;bottom:0;width:100%;height:34px;background:var(--navy);color:#fff;font-size:9px;font-weight:600;letter-spacing:.3px;display:flex;align-items:center;justify-content:center}
.footer__line{position:absolute;left:0;top:0;width:100%;height:2px;background:linear-gradient(90deg,var(--green-line) 0 33.3%,var(--navy) 33.3% 66.6%,var(--orange) 66.6%)}
.habit-box{left:25px;top:151px;width:189px;height:83px;background:var(--green);border-radius:3px}
.habit-box h3{position:absolute;left:43px;top:14px;font-size:11.5px;font-weight:500;color:var(--navy)}
.habit-box p{position:absolute;left:43px;top:35px;width:140px;font-size:8.3px;line-height:1.25;font-weight:300;color:#3a4a35}
.habit-box .eye{position:absolute;left:9px;top:38px}
.contact{left:231px;top:340px;width:231px;text-align:center;color:#fff;font-size:9px;line-height:1.25;z-index:2}
.contact b{font-weight:600}
.contact .ico{display:block;margin:0 auto 4px}
.contact .row{margin-bottom:9px}
.option-head{position:absolute;top:0;height:80px;display:flex;align-items:center;justify-content:center;text-align:center;font-size:16px;line-height:1.2;font-weight:500}
.review{left:33px;top:368px;width:626px;height:116px;background:#f1f1f2;border-radius:4px}
.stars{position:absolute;left:416px;top:12px;color:var(--orange);font-size:16px;letter-spacing:3px}
</style>
</head>
<body>

<section class="sheet sheet--outer">
  <h2 class="abs panel-title" style="left:26px;top:41px;font-size:16px">Healty Lifestyle Habits</h2>
  <p class="abs body" style="left:26px;top:83px;width:185px">Too much screen time and prolonged near work, especially at very close distances, may worsen nearsightedness. We recommend limiting non-academic screen use and following:</p>
  <div class="abs habit-box">
    <svg class="eye" width="27" height="27" viewBox="0 0 27 27"><circle cx="13.5" cy="13.5" r="13.5" fill="var(--navy)"/><path d="M5.5 13.5c2.2-3.6 5-5.3 8-5.3s5.8 1.7 8 5.3c-2.2 3.6-5 5.3-8 5.3s-5.8-1.7-8-5.3z" fill="none" stroke="#fff" stroke-width="1.5"/><circle cx="13.5" cy="13.5" r="2.4" fill="#fff"/></svg>
    <h3>THE 20-20-20 RULE</h3>
    <p>Every 20 minutes, take a 20-second break and look at something at least 20 ft away.</p>
  </div>
  <p class="abs body body--just" style="left:28px;top:248px;width:182px">Healthy daily habits can help slow myopia progression. Studies show children who spend at least 2 hours outdoors daily are less likely to develop myopia and may experience slower progression.</p>

  <div class="abs brand" style="left:298px;top:48px"><span class="brand__dot"></span>Brookhollow Kids Vision</div>
  <h2 class="abs panel-title" style="left:231px;top:90px;width:231px;text-align:center;font-size:15px;line-height:1.25">Expert Care<br>For Children Vision</h2>
  <div class="abs rule" style="left:336px;top:130px;background:var(--gold)"></div>
  <div class="photo" role="img" aria-label="Bright clinic reception area with curved front desk" style="left:242px;top:149px;width:206px;height:124px;background:linear-gradient(160deg,#f3f4f6,#d9dde2 55%,#c9b08e)"></div>
  <p class="abs" style="left:231px;top:286px;width:231px;text-align:center;font-size:11px;letter-spacing:3px;color:#333">CONTACT</p>

  <div class="abs brand" style="left:512px;top:48px;font-size:12.5px"><span class="brand__dot"></span>Brookhollow Kids Vision</div>
  <h1 class="abs" style="left:462px;top:92px;width:231px;text-align:center;color:var(--navy);font-weight:600;font-size:38px;line-height:.95;letter-spacing:.5px">MYOPIA<br><span style="font-size:32px">CONTROL</span></h1>
  <p class="abs body body--just" style="left:480px;top:188px;width:186px">helps slow eye growth, keep glasses prescriptions lower, and reduce the risk of eye disease in adulthood.</p>
  <div class="abs rule" style="left:562px;top:225px"></div>
  <p class="abs body body--just" style="left:480px;top:239px;width:186px">Myopia causes blurry distance vision because the eye elongates and usually worsens throughout childhood. It is becoming increasingly common. Higher myopia &amp; stronger glasses prescriptions increase the risk of retinal problems and macular degeneration in adulthood.</p>

  <div class="photo" role="img" aria-label="Girl lying by a window using a tablet" style="left:0;top:315px;width:231px;height:189px;background:linear-gradient(120deg,#9fb58a,#d8dcd6 45%,#b7b3ad)"></div>
  <div class="photo" style="left:231px;top:315px;width:231px;height:189px;background:var(--navy)"></div>
  <div class="photo" role="img" aria-label="Close-up of a child wearing glasses" style="left:462px;top:315px;width:230px;height:189px;background:linear-gradient(100deg,#e9d6cb,#f2e4dc 50%,#d8c2b6)"></div>
  <svg class="abs" style="left:0;top:0" width="692" height="360" viewBox="0 0 692 360">
    <path d="M0 315 L0 336 C80 343 160 350 231 350 C300 325 390 318 462 338 C545 356 620 343 692 324 L692 315 Z" fill="#fff"/>
    <path d="M0 336 C80 343 160 350 231 350" fill="none" stroke="var(--green-line)" stroke-width="2"/>
    <path d="M231 350 C300 325 390 318 462 338" fill="none" stroke="var(--gold)" stroke-width="2"/>
    <path d="M462 338 C545 356 620 343 692 324" fill="none" stroke="var(--orange)" stroke-width="2"/>
  </svg>
  <div class="abs contact">
    <div class="row"><svg class="ico" width="11" height="11" viewBox="0 0 11 11"><circle cx="5.5" cy="5.5" r="5.5" fill="#fff"/><path d="M3.6 3c.4-.3.7-.2.9.2l.4.8c.1.3 0 .5-.2.7l-.3.2c.3.7.8 1.2 1.5 1.5l.2-.3c.2-.2.4-.3.7-.2l.8.4c.4.2.5.5.2.9-.5.7-1.3.8-2.1.3-1.1-.6-2-1.5-2.6-2.6-.4-.8-.2-1.5.5-1.900z" fill="var(--navy)"/></svg><b>Voice:</b> (555) 214-0382</div>
    <div class="row"><svg class="ico" width="11" height="11" viewBox="0 0 11 11"><circle cx="5.5" cy="5.5" r="5.5" fill="#fff"/><path d="M3.6 3c.4-.3.7-.2.9.2l.4.8c.1.3 0 .5-.2.7l-.3.2c.3.7.8 1.2 1.5 1.5l.2-.3c.2-.2.4-.3.7-.2l.8.4c.4.2.5.5.2.9-.5.7-1.3.8-2.1.3-1.1-.6-2-1.5-2.6-2.6-.4-.8-.2-1.5.5-1.9z" fill="var(--navy)"/></svg><b>Text:</b> (555) 214-0397</div>
    <div class="row"><svg class="ico" width="11" height="11" viewBox="0 0 11 11"><circle cx="5.5" cy="5.5" r="5.5" fill="#fff"/><rect x="3" y="3.7" width="5" height="3.6" fill="none" stroke="var(--navy)" stroke-width=".8"/><path d="M3 3.8l2.5 2 2.5-2" fill="none" stroke="var(--navy)" stroke-width=".8"/></svg>appointments@brookhollowkidsvision.com</div>
    <div class="row"><svg class="ico" width="11" height="11" viewBox="0 0 11 11"><circle cx="5.5" cy="5.5" r="5.5" fill="#fff"/><path d="M5.5 2.6a2 2 0 0 1 2 2c0 1.5-2 3.6-2 3.6s-2-2.1-2-3.6a2 2 0 0 1 2-2z" fill="var(--navy)"/><circle cx="5.5" cy="4.6" r=".7" fill="#fff"/></svg>Brookhollow Kids Vision<br>218 Alder Crest Road<br>Fairmont Bay, NC 27801</div>
  </div>
  <div class="footer"><span class="footer__line"></span>WWW.BROOKHOLLOWKIDSVISION.COM</div>
</section>

<section class="sheet sheet--inner">
  <svg class="abs" style="left:0;top:0" width="692" height="90" viewBox="0 0 692 90">
    <path d="M0 0 H231 V70 C160 80 70 90 0 70 Z" fill="var(--green)"/>
    <path d="M231 0 H462 V72 C400 58 330 52 290 60 C270 64 250 68 231 70 Z" fill="var(--peach)"/>
    <path d="M462 0 H692 V68 C620 80 540 85 462 72 Z" fill="var(--lavender)"/>
  </svg>
  <h2 class="option-head" style="left:0;width:231px;color:#3b4a3a;padding-top:6px">Luminar Corvane<br>glasses lenses</h2>
  <h2 class="option-head" style="left:231px;width:231px;color:var(--navy);height:62px">Low-dose Atropine</h2>
  <h2 class="option-head" style="left:462px;width:230px;color:#3d3b4a;height:74px">Specialty<br>Contact Lenses</h2>

  <p class="abs body" style="left:31px;top:111px;width:178px">FDA market authorized Luminar Corvane glasses lenses have been shown to <b>slow myopia progression by about 50% in children aged 6-12.</b></p>
  <p class="abs body" style="left:31px;top:167px;width:178px">These lenses are a great treatment option because all your child needs to do is wear glasses. They look almost identical to ordinary glasses, but use specialized optics to signal the brain to slow the growth of myopic eyes.</p>
  <p class="abs body" style="left:256px;top:111px;width:192px">These eyedrops have been studied for over 20 years and have been shown to <b>slow myopia progression by about 50% when used consistently.</b></p>
  <p class="abs body" style="left:256px;top:167px;width:192px">Low-dose atropine is simple to add to your daily routine. One drop is placed in each eye before bed each evening. These are ordered from a compounding pharmacy &amp; mailed directly to your home.</p>
  <p class="abs body" style="left:483px;top:111px;width:188px">FDA-approved ClearPath lenses have been shown to <b>slow myopia progression by about 50% in children aged 8-12.</b></p>
  <p class="abs body" style="left:483px;top:167px;width:188px">Contact lenses can be a great fit for many children, especially active children or those who do not enjoy wearing glasses. Many children as young as 7 or 8 are successful at wearing contacts</p>

  <div class="photo" role="img" aria-label="Close-up of a lens with concentric optical rings" style="left:31px;top:241px;width:171px;height:98px;background:linear-gradient(135deg,#7d97a6,#c9d6dc 50%,#6f8796)"></div>
  <div class="photo" role="img" aria-label="Doctor placing eye drops for a young child" style="left:264px;top:246px;width:171px;height:88px;background:linear-gradient(120deg,#eef0ee,#e4dcd4 50%,#c8b8a8)"></div>
  <div class="photo" role="img" aria-label="Smiling child holding a contact lens on a fingertip" style="left:487px;top:248px;width:166px;height:91px;background:linear-gradient(120deg,#f3ede8,#e3c6ad 50%,#f1ece8)"></div>

  <div class="abs review">
    <div class="abs brand" style="left:35px;top:50px;font-size:12.5px"><span class="brand__dot"></span>Brookhollow Kids Vision</div>
    <div class="stars">★★★★★</div>
    <p class="abs body" style="left:225px;top:39px;width:385px;line-height:1.3">Everyone at Brookhollow Kids Vision was very nice and accommodating. They made us feel comfortable as soon as we walked in the door. Dr. Evan Marsh was professional, yet had a warm personality and was great with my 2 yr old daughter and explained everything so we could easily understand it. Our entire experience there with everyone was just great. highly recommend this practice<br><b style="color:var(--navy)">Dana Whitfield</b></p>
  </div>
  <div class="footer"><span class="footer__line"></span>WWW.BROOKHOLLOWKIDSVISION.COM</div>
</section>

</body>
</html>
```